Lifestyle brand needs lip balm label design

We need a label design for lip balm tubes. The name of our company is "lorvanquill"

Design Description:
Our lip balm tubes will be black. The label itself will be clear/transparent. We would like to create a gradient effect with the color green (same shade as our logo) starting from the bottom and slowly fading out to clear so that the black tube is visible (example of gradient shown in attached image)

We have two lip balm flavors: mint and lemongrass.
We would like the top/clear portion of the label to say "MINT" (all caps) . The second label should say "LEMONGRASS" (all caps) in the same location. Our logo "lorvanquill" should be in the bottom/green portion of the label. Below the logo, we would like the words "NATURAL BALM" (all caps) in white text

```html
<!DOCTYPE html>
<html lang="en">
<head>
<meta charset="UTF-8">
<title>lorvanquill natural balm labels</title>
<link rel="stylesheet" href="https://fonts.googleapis.com/css2?family=Montserrat:wght@300;400&display=swap">
<style>
  :root {
    --canvas: #ffffff;
    --label-top: #28261f;
    --label-upper: #3f4a1a;
    --label-mid: #5c7f16;
    --label-low: #6f951c;
    --label-bottom: #a4c03a;
    --flavour-text: #ffffff;
    --brand-text: #2a2a22;
    --tagline-text: #ffffff;
    --herb-tone: rgba(200, 225, 140, 0.16);
  }
  * { margin: 0; padding: 0; box-sizing: border-box; }
  html, body {
    width: 1200px;
    height: 1200px;
    overflow: hidden;
    background: var(--canvas);
  }
  .canvas {
    position: relative;
    width: 1200px;
    height: 1200px;
    font-family: 'Montserrat', sans-serif;
  }
  .label {
    position: absolute;
    top: 227px;
    width: 400px;
    height: 746px;
    background: linear-gradient(to bottom,
      var(--label-top) 0%,
      var(--label-upper) 22%,
      var(--label-mid) 45%,
      var(--label-low) 62%,
      var(--label-bottom) 100%);
    overflow: hidden;
  }
  .label--mint { left: 164px; }
  .label--lemongrass { left: 635px; }
  .label__herb {
    position: absolute;
    border-radius: 50% 50% 45% 45%;
    background: radial-gradient(ellipse at center, var(--herb-tone) 0%, rgba(200,225,140,0) 72%);
  }
  .label--mint .label__herb { left: 86px; top: 443px; width: 215px; height: 280px; }
  .label--lemongrass .label__herb { left: 119px; top: 465px; width: 160px; height: 300px; }
  .label__flavour {
    position: absolute;
    top: 248px;
    width: 100%;
    text-align: center;
    color: var(--flavour-text);
    font-weight: 300;
    font-size: 42px;
    letter-spacing: 1px;
  }
  .label__brand {
    position: absolute;
    top: 548px;
    width: 100%;
    text-align: center;
    color: var(--brand-text);
    font-weight: 400;
    font-size: 54px;
    letter-spacing: 0.5px;
  }
  .label__tagline {
    position: absolute;
    top: 635px;
    width: 100%;
    text-align: center;
    color: var(--tagline-text);
    font-weight: 400;
    font-size: 25px;
    letter-spacing: 0.5px;
  }
</style>
</head>
<body>
  <main class="canvas">
    <section class="label label--mint">
      <div class="label__herb" role="img" aria-label="Faint line illustration of a mint leaf"></div>
      <p class="label__flavour">MINT</p>
      <p class="label__brand">lorvanquill</p>
      <p class="label__tagline">NATURAL BALM</p>
    </section>
    <section class="label label--lemongrass">
      <div class="label__herb" role="img" aria-label="Faint line illustration of lemongrass stalks"></div>
      <p class="label__flavour">LEMONGRASS</p>
      <p class="label__brand">lorvanquill</p>
      <p class="label__tagline">NATURAL BALM</p>
    </section>
  </main>
</body>
</html>
```